VOLTA NUB (Disposable Charger) Needs packaging with actual mock up!

We have a word document with all the information that we need on the package so feel free to be creative and design your own. It is a small condom wrapper for a one-time use phone charger.

Below I have attached the file with the dimensions of the package. And also some competitors packaging for examples only. Please don't copy them. We need to be different and cooler.

Our logo is also below called Volta Nub(See charger for logo we want). The other ones are just examples.

```html
<!DOCTYPE html>
<html lang="en">
<head>
<meta charset="utf-8">
<title>Volta Nub – Disposable Charger Wrappers</title>
<link rel="stylesheet" href="https://fonts.googleapis.com/css2?family=League+Spartan:wght@700&family=Josefin+Sans:wght@300;400&family=Comfortaa:wght@700&family=Exo+2:wght@700&display=swap">
<style>
  :root {
    --teal: #7dfde9;
    --green: #6cc46a;
    --ink: #060606;
    --paper: #ffffff;
    --tab: #e2e2e2;
  }
  * { margin: 0; padding: 0; box-sizing: border-box; }
  html, body { width: 1200px; height: 800px; overflow: hidden; background: var(--paper); }
  .canvas { position: relative; width: 1200px; height: 800px; }

  .pack {
    position: absolute; top: 136px; width: 486px; height: 568px;
    background: var(--pack-bg); color: var(--pack-fg);
    box-shadow: 0 2px 10px rgba(0,0,0,0.12);
  }
  .pack--dark { left: 96px; --pack-bg: var(--ink); --pack-fg: var(--paper); }
  .pack--light { left: 625px; --pack-bg: var(--paper); --pack-fg: var(--ink); }

  .pack__tab {
    position: absolute; top: 115px; width: 16px; height: 11px;
    background: var(--tab); border-radius: 6px;
  }
  .pack__tab--left { left: 0; border-radius: 0 6px 6px 0; }
  .pack__tab--right { right: 0; border-radius: 6px 0 0 6px; }

  .brand {
    position: absolute; left: 49px; top: 46px; width: 162px;
  }
  .brand__name {
    display: flex; align-items: center; gap: 6px;
    font-family: "League Spartan", sans-serif; font-weight: 700;
    font-size: 29px; letter-spacing: 0.5px; line-height: 1; color: var(--pack-fg);
  }
  .brand__dot { width: 9px; height: 9px; background: var(--green); flex: none; }
  .brand__rule { margin-top: 8px; height: 2px; width: 106px; background: var(--green); }

  .port-badge {
    position: absolute; left: 312px; top: 38px; width: 128px; height: 55px;
    border-radius: 28px; display: flex; flex-direction: column;
    align-items: center; justify-content: center;
    font-family: "Exo 2", sans-serif; font-weight: 700; line-height: 1.02; text-align: center;
  }
  .pack--dark .port-badge { border: 3px solid var(--teal); color: var(--teal); }
  .pack--light .port-badge { background: var(--teal); color: var(--ink); }
  .port-badge__main { font-size: 14px; }
  .port-badge__sub { font-size: 12px; }

  .tagline {
    position: absolute; left: 40px; top: 142px; width: 410px;
    display: flex; justify-content: space-between;
    font-family: "Comfortaa", sans-serif; font-weight: 700; font-size: 23px;
    letter-spacing: 1px; white-space: nowrap;
  }
  .tagline__item::before { content: "•"; margin-right: 10px; }

  .product-panel { position: absolute; left: 44px; top: 186px; width: 398px; height: 228px; }

  .capacity {
    position: absolute; left: 131px; top: 441px; width: 222px; height: 31px;
    background: var(--teal); border-radius: 10px; color: var(--ink);
    font-family: "Comfortaa", sans-serif; font-weight: 700; font-size: 19px;
    display: flex; align-items: center; justify-content: center; letter-spacing: 0.5px;
  }
  .eco {
    position: absolute; left: 73px; top: 481px; display: flex; align-items: center; gap: 12px;
    font-family: "Comfortaa", sans-serif; font-weight: 700; font-size: 25px; letter-spacing: 1.2px;
  }
  .eco__icon { width: 36px; height: 36px; }
  .site {
    position: absolute; left: 0; right: 0; top: 522px; text-align: center;
    font-family: "Josefin Sans", sans-serif; font-weight: 400; font-size: 19px; letter-spacing: 2px;
  }
</style>
</head>
<body>
<main class="canvas">

  <section class="pack pack--dark">
    <span class="pack__tab pack__tab--left"></span>
    <span class="pack__tab pack__tab--right"></span>
    <div class="brand">
      <div class="brand__name"><span>VOLTA NUB</span><span class="brand__dot"></span></div>
      <div class="brand__rule"></div>
    </div>
    <div class="port-badge">
      <span class="port-badge__main">Micro USB Port</span>
      <span class="port-badge__sub">Compatible</span>
      <span class="port-badge__sub">with Andros</span>
    </div>
    <p class="tagline"><span class="tagline__item">Charged Up</span><span class="tagline__item">Ready for Use</span></p>
    <svg class="product-panel" viewBox="0 0 398 228" aria-label="One time use phone charger">
      <path d="M1.5 42 V32 A30.5 30.5 0 0 1 32 1.5 H366 A30.5 30.5 0 0 1 396.5 32 V42 Z" fill="#060606" stroke="#7dfde9" stroke-width="3"/>
      <path d="M0 42 H398 V176 A52 52 0 0 1 346 228 H52 A52 52 0 0 1 0 176 Z" fill="#7dfde9"/>
      <text x="28" y="36" font-family="Josefin Sans, sans-serif" font-weight="300" font-size="29" fill="#7dfde9" textLength="176">One time use</text>
      <text x="22" y="122" font-family="League Spartan, sans-serif" font-weight="700" font-size="78" fill="#060606" textLength="262" lengthAdjust="spacingAndGlyphs">PHONE</text>
      <text x="22" y="196" font-family="League Spartan, sans-serif" font-weight="700" font-size="78" fill="#060606" textLength="350" lengthAdjust="spacingAndGlyphs">CHARGER</text>
    </svg>
    <div class="capacity">2900mah</div>
    <p class="eco">
      <svg class="eco__icon" viewBox="0 0 36 36" role="img" aria-label="Recycling symbol"><circle cx="18" cy="18" r="15" fill="#ffffff"/></svg>
      <span>Bio-degradable shell</span>
    </p>
    <p class="site">www.volta-nub.com</p>
  </section>

  <section class="pack pack--light">
    <span class="pack__tab pack__tab--left"></span>
    <span class="pack__tab pack__tab--right"></span>
    <div class="brand">
      <div class="brand__name"><span>VOLTA NUB</span><span class="brand__dot"></span></div>
      <div class="brand__rule"></div>
    </div>
    <div class="port-badge">
      <span class="port-badge__main">Micro USB Port</span>
      <span class="port-badge__sub">Compatible</span>
      <span class="port-badge__sub">with Andros</span>
    </div>
    <p class="tagline"><span class="tagline__item">Charged Up</span><span class="tagline__item">Ready for Use</span></p>
    <svg class="product-panel" viewBox="0 0 398 228" aria-label="One time use phone charger">
      <path d="M1.5 42 V32 A30.5 30.5 0 0 1 32 1.5 H366 A30.5 30.5 0 0 1 396.5 32 V42 Z" fill="#060606" stroke="#7dfde9" stroke-width="3"/>
      <path d="M0 42 H398 V176 A52 52 0 0 1 346 228 H52 A52 52 0 0 1 0 176 Z" fill="#7dfde9"/>
      <text x="28" y="36" font-family="Josefin Sans, sans-serif" font-weight="300" font-size="29" fill="#7dfde9" textLength="176">One time use</text>
      <text x="22" y="122" font-family="League Spartan, sans-serif" font-weight="700" font-size="78" fill="#060606" textLength="262" lengthAdjust="spacingAndGlyphs">PHONE</text>
      <text x="22" y="196" font-family="League Spartan, sans-serif" font-weight="700" font-size="78" fill="#060606" textLength="350" lengthAdjust="spacingAndGlyphs">CHARGER</text>
    </svg>
    <div class="capacity">2900mah</div>
    <p class="eco">
      <svg class="eco__icon" viewBox="0 0 36 36" role="img" aria-label="Recycling symbol"><circle cx="18" cy="18" r="15" fill="#060606"/></svg>
      <span>Bio-degradable shell</span>
    </p>
    <p class="site">www.voltanub.com</p>
  </section>

</main>
</body>
</html>
```